AMAZING WEBSITE DESIGN NEEDED FOR MAID / CLEANING SERVICE

NOTE: This is Website Design Only - No coding required

Please submit your designs ASAP as we want to pick a winner and get started!

Hey,

We are looking for a new amazing website design for a maid or cleaning service.

They have a horrible website that we want turned into a masterpiece.

As you will see on their current site:

http://tidyharborco.examplehost.net/

They have a lot of stuff, very disorganized, and need help.

Here is what we need:

Colors: Same as current site, Orange, Gray, Black

Menu: Horizontal with same Menu items

Need a spot for a video on the homepage

Want content to be structured in a great format that is easy to read.

Want to highlight commercial and residential on the website homepage.

Also want a spot for customer testimonials

We want the site clean, professional, fresh and modern.

Please help by matching the logo design.

I look forward to your designs!
Updates

Hi All! Really appreciate your efforts and designs. I will be meeting with our client on Monday and will then be able to provide feedback after our meeting. If you have other ideas, please submit them. The more I can show him the better! Thanks!

Target Market(s)

The target market is residential home owners as well as commercial businesses who need cleaning on a regular basis.

This company cleans homes and offices for individuals.

Industry/Entity Type

Residential

Font styles to use
Sans Serif

Requirements
Must have
• Must match logo colors
Must have spot for video
Must have a clean look
Must have a bold look
Nice to have
• Highly visual
Should not have
• clutter
messy design
hard to read

```html
<!DOCTYPE html>
<html lang="en">
<head>
<meta charset="utf-8">
<title>Tidy Harbor — Quality Commercial & Residential Cleaning</title>
<link rel="stylesheet" href="https://fonts.googleapis.com/css2?family=Open+Sans:ital,wght@0,400;0,600;0,700;1,400&family=Roboto+Slab:wght@400&display=swap">
<style>
  :root{
    --orange:#f07a1a;
    --orange-deep:#e0620e;
    --nav-top:#f7901e;
    --nav-bottom:#ee7412;
    --ink:#3a3a3a;
    --muted:#6b6b6b;
    --line:#e2e2e2;
    --charcoal:#3b3b3b;
    --coal:#262626;
    --paper:#ffffff;
    --band:#f3f3f3;
    --hero-light:#ece4d2;
    --hero-warm:#d9a24c;
  }
  *{box-sizing:border-box;margin:0;padding:0}
  html,body{width:673px;height:1200px;overflow:hidden;background:var(--paper)}
  body{font-family:"Open Sans",Arial,sans-serif;color:var(--ink);position:relative}

  /* header */
  .site-header{position:absolute;left:0;top:0;width:673px;height:82px}
  .brand{position:absolute;left:57px;top:24px;display:flex;align-items:center;gap:6px}
  .brand-mark{width:18px;height:18px;background:var(--orange)}
  .brand-name{font-size:21px;font-weight:700;color:var(--orange);letter-spacing:-.3px}
  .brand-tagline{position:absolute;left:78px;top:61px;font-size:6.5px;color:var(--muted);font-style:italic}
  .call{position:absolute;right:57px;top:10px;text-align:right;line-height:13px}
  .call-label{font-size:10px;color:var(--muted)}
  .call-number{font-size:11px;color:var(--orange);font-weight:600}
  .search{position:absolute;right:57px;top:44px;width:88px;height:17px;border:1px solid var(--line);display:flex;align-items:center}
  .search span{flex:1;font-size:7.5px;color:#999;padding-left:14px}
  .search i{width:18px;height:15px;border-left:1px solid var(--line);display:flex;align-items:center;justify-content:center}

  /* nav */
  .main-nav{position:absolute;left:0;top:82px;width:673px;height:27px;background:linear-gradient(var(--nav-top),var(--nav-bottom))}
  .main-nav ul{list-style:none;display:flex;position:absolute;left:57px;top:0;height:27px}
  .main-nav li{height:27px;display:flex;align-items:center;justify-content:center;font-size:8.8px;color:#fff;border-right:1px solid rgba(255,255,255,.25)}
  .main-nav li.active{background:#4a4a4a}

  /* hero */
  .hero{position:absolute;left:0;top:109px;width:673px;height:341px;background:linear-gradient(100deg,var(--hero-light) 0%,var(--hero-warm) 100%)}
  .hero-caption{position:absolute;left:0;bottom:0;width:673px;height:45px;background:rgba(40,40,40,.78);color:#fff;text-align:center;font-size:10.5px;font-weight:600;line-height:15px;padding-top:7px}
  .hero-arrow{position:absolute;top:149px;width:31px;height:41px;background:rgba(90,90,90,.7);display:flex;align-items:center;justify-content:center}

  /* specials */
  .specials-text{position:absolute;left:0;top:472px;width:673px;text-align:center;font-size:14.5px;color:#444}
  .btn-offers{position:absolute;left:267px;top:498px;width:139px;height:23px;background:var(--orange);color:#fff;font-size:10px;font-weight:600;border-radius:2px;display:flex;align-items:center;justify-content:center}

  /* audience panels */
  .panel{position:absolute;top:546px;width:336px;height:132px}
  .panel-corporate{left:0;background:linear-gradient(180deg,#b8b3cc 0%,#8c88a6 55%,#4f5a70 100%)}
  .panel-residential{left:337px;background:linear-gradient(90deg,#dcdcdc,#f0f0f0 60%,#e6e6e6)}
  .panel-title{position:absolute;font-size:17.5px;white-space:nowrap;line-height:22px}
  .panel-corporate .panel-title{left:63px;top:10px;background:rgba(70,70,70,.85);color:#fff;padding:0 5px}
  .panel-residential .panel-title{right:59px;top:75px;color:var(--orange-deep)}
  .read-more{position:absolute;font-family:"Roboto Slab",Georgia,serif;font-size:11px;line-height:20px;color:#333;background:#fff;padding:0 10px}
  .panel-corporate .read-more{left:63px;top:36px;background:#eee}
  .panel-residential .read-more{right:59px;top:100px;color:var(--orange-deep)}

  /* welcome */
  .welcome h1{position:absolute;left:57px;top:705px;font-size:15px;font-weight:600;color:var(--orange-deep)}
  .welcome p{position:absolute;left:57px;top:731px;width:384px;font-size:7.3px;line-height:13px;color:var(--muted)}
  .video{position:absolute;left:454px;top:710px;width:162px;height:94px;background:linear-gradient(120deg,#b6b1ac,#d3cec9 50%,#9a9591)}
  .video svg{position:absolute;left:63px;top:29px}

  /* features */
  .features{position:absolute;left:0;top:836px;width:673px;height:104px;background:var(--band);border-top:1px solid #e8e8e8;border-bottom:1px solid #e8e8e8}
  .feature{position:absolute;top:27px;width:180px}
  .feature-icon{position:absolute;left:0;top:0;width:51px;height:51px;border-radius:50%;background:var(--orange);display:flex;align-items:center;justify-content:center}
  .feature h2{position:absolute;left:57px;top:-4px;font-size:14px;font-weight:600;color:var(--orange-deep);white-space:nowrap}
  .feature p{position:absolute;left:58px;top:17px;width:112px;font-size:7px;line-height:10.4px;color:#888}

  /* testimonials */
  .testimonials h2{position:absolute;left:0;top:960px;width:673px;text-align:center;font-size:14.5px;font-weight:600;color:var(--orange-deep)}
  .avatar{position:absolute;left:72px;top:988px;width:68px;height:68px;border-radius:50%;background:radial-gradient(circle at 50% 45%,#e5c7ae,#cfd3d6 70%);box-shadow:0 2px 3px rgba(0,0,0,.15)}
  .quote{position:absolute;left:153px;top:993px;width:452px;font-size:8.3px;line-height:14px;font-style:italic;color:#555}
  .quote-name{position:absolute;left:153px;top:1038px;font-size:8.5px;color:var(--orange-deep)}
  .t-arrow{position:absolute;top:997px}

  /* footer */
  .site-footer{position:absolute;left:0;top:1085px;width:673px;height:73px;background:var(--charcoal);color:#ddd;font-size:7.8px}
  .foot-col{position:absolute;top:9px;line-height:15.3px;list-style:none}
  .foot-col li::before{content:"•";color:#999;margin-right:5px}
  .foot-text{position:absolute;line-height:15.3px}
  .social{position:absolute;left:525px;top:37px;display:flex;gap:3px}
  .social span{width:16px;height:16px;border-radius:50%;background:#8a8a8a}
  .legal{position:absolute;left:0;top:1158px;width:673px;height:42px;background:var(--coal);color:#aaa;font-size:7.8px;text-align:center;line-height:42px}
</style>
</head>
<body>

<header class="site-header">
  <div class="brand"><span class="brand-mark"></span><span class="brand-name">Tidy Harbor</span></div>
  <div class="brand-tagline">Quality Commercial &amp; Residential Cleaning</div>
  <div class="call">
    <div class="call-label">Call us</div>
    <div class="call-number">(555) 014-2290</div>
  </div>
  <div class="search"><span>Search</span><i><svg width="9" height="9" viewBox="0 0 10 10"><circle cx="4" cy="4" r="3" fill="none" stroke="#888" stroke-width="1.4"/><line x1="6.2" y1="6.2" x2="9.2" y2="9.2" stroke="#888" stroke-width="1.6"/></svg></i></div>
</header>

<nav class="main-nav">
  <ul>
    <li class="active" style="width:50px">HOME</li>
    <li style="width:66px">ABOUT US</li>
    <li style="width:61px">SERVICES</li>
    <li style="width:71px">OUR STAFFS</li>
    <li style="width:57px">WHY US?</li>
    <li style="width:86px">TESTIMONIALS</li>
    <li style="width:90px">SPECIAL OFFERS</li>
    <li style="width:80px">CONTACT US</li>
  </ul>
</nav>

<section class="hero" role="img" aria-label="Photo of a bright, freshly cleaned modern kitchen and living space">
  <div class="hero-arrow" style="left:0"><svg width="14" height="26" viewBox="0 0 14 26"><polyline points="12,1 2,13 12,25" fill="none" stroke="#fff" stroke-width="1.3"/></svg></div>
  <div class="hero-arrow" style="right:0"><svg width="14" height="26" viewBox="0 0 14 26"><polyline points="2,1 12,13 2,25" fill="none" stroke="#fff" stroke-width="1.3"/></svg></div>
  <div class="hero-caption">Locally Owned &amp; Operated<br>Never deal with an unresponsive franchise - Deal with the owner!</div>
</section>

<p class="specials-text">We currently have spectacular, unheard of, specials going on right now!</p>
<div class="btn-offers">View Our Special Offers</div>

<section class="panel panel-corporate" role="img" aria-label="Photo of a modern corporate office lobby">
  <div class="panel-title">CORPORATE OWNERS</div>
  <div class="read-more">Read more</div>
</section>
<section class="panel panel-residential" role="img" aria-label="Photo of a bright white residential bedroom">
  <div class="panel-title">RESIDENTIAL OWNERS</div>
  <div class="read-more">Read more</div>
</section>

<section class="welcome">
  <h1>Welcome to Tidy Harbor</h1>
  <p>Thank you for visiting us! You are one step closer to experiencing first class maid service! Our company specializes in detailed housekeeping, janitorial, and commerical cleaning services making your environment shine and sparkle like it never has before! &nbsp;Our maids are fully trained professionals who we recruit from high end luxury hotels we know, like the Grand Alder and Bellmoor! We pride ourselves in delivering exceptional service to our valued customers by fully understanding what your expectations &amp; needs are! We will strive for perfection and we will provide an uncompromising commitment to excellence!</p>
  <div class="video" role="img" aria-label="Video thumbnail of a cleaner wiping a countertop">
    <svg width="36" height="36" viewBox="0 0 36 36"><circle cx="18" cy="18" r="16" fill="rgba(0,0,0,.25)" stroke="#fff" stroke-width="2.5"/><polygon points="14,10 26,18 14,26" fill="#fff"/></svg>
  </div>
</section>

<section class="features">
  <div class="feature" style="left:57px">
    <div class="feature-icon"><svg width="30" height="30" viewBox="0 0 30 30"><circle cx="15" cy="15" r="12" fill="none" stroke="#fff" stroke-width="3"/><ellipse cx="15" cy="15" rx="5" ry="12" fill="none" stroke="#fff" stroke-width="2"/><line x1="3" y1="15" x2="27" y2="15" stroke="#fff" stroke-width="2"/></svg></div>
    <h2>Eco Friendly</h2>
    <p>Tidy Harbor is commited to using Eco Green chemicals to keep you and your family safe! No harsh chemicals here!</p>
  </div>
  <div class="feature" style="left:249px">
    <div class="feature-icon"><svg width="26" height="30" viewBox="0 0 26 30"><path d="M3 2h20v26l-3-2-3 2-4-2-4 2-3-2-3 2z" fill="#fff"/><text x="6" y="19" font-family="Open Sans,sans-serif" font-size="12" font-weight="700" fill="#f07a1a">$</text><rect x="14" y="9" width="6" height="2" fill="#f07a1a"/><rect x="14" y="14" width="6" height="2" fill="#f07a1a"/><rect x="14" y="19" width="6" height="2" fill="#f07a1a"/></svg></div>
    <h2>We Donate</h2>
    <p>Tidy Harbor is commited to using Eco Green chemicals to keep you and your family safe! No harsh chemicals here!</p>
  </div>
  <div class="feature" style="left:441px">
    <div class="feature-icon"><svg width="30" height="30" viewBox="0 0 30 30"><rect x="3" y="13" width="6" height="13" rx="1" fill="#fff"/><path d="M11 13l5-9c2 0 3 1 3 3l-1 5h7c2 0 3 2 2 3l-3 10c0 1-1 2-3 2H11z" fill="#fff"/></svg></div>
    <h2>100% Satisfaction</h2>
    <p>Tidy Harbor is commited to using Eco Green chemicals to keep you and your family safe! No harsh chemicals here!</p>
  </div>
</section>

<section class="testimonials">
  <h2>Testimonials</h2>
  <svg class="t-arrow" style="left:23px" width="12" height="18" viewBox="0 0 12 18"><polyline points="10,1 2,9 10,17" fill="none" stroke="#888" stroke-width="1.6"/></svg>
  <svg class="t-arrow" style="left:638px" width="12" height="18" viewBox="0 0 12 18"><polyline points="2,1 10,9 2,17" fill="none" stroke="#888" stroke-width="1.6"/></svg>
  <div class="avatar" role="img" aria-label="Portrait photo of the customer"></div>
  <p class="quote">“ &nbsp;Nam a malesuada libero. Duis sodales et libero vel interdum. Interdum et malesuada fames ac ante ipsum primis in faucibus. Donec lobortis dui tortor, eu lobortis felis mattis nec. Sed justo quam, luctus eu mauris eget, euismod dapibus sem. Sed tempus feugiat ante, at ornare libero volutpat sed. Maecenas quis magna magna. &nbsp;”</p>
  <div class="quote-name">Dana Mercer, NY</div>
</section>

<footer class="site-footer">
  <ul class="foot-col" style="left:57px"><li>Home</li><li>About us</li><li>Services</li><li>Our Staffs</li></ul>
  <ul class="foot-col" style="left:134px"><li>Why us?</li><li>Testimonials</li><li>Special Offers</li><li>Contact us</li></ul>
  <div class="foot-text" style="left:241px;top:6px">4120 Lantern Ridge Road<br>NE Suite 310<br>Cedar Falls<br>New Mexico &nbsp;| &nbsp;87000</div>
  <div class="foot-text" style="left:364px;top:16px">Call : (555) 014-2290<br>Fax : (555) 014-7731<br>E-mail : hello@tidyharbor.example</div>
  <div class="foot-text" style="left:525px;top:21px">Connect with us</div>
  <div class="social"><span></span><span></span><span></span><span></span><span></span></div>
</footer>
<div class="legal">Copyright &nbsp;© &nbsp;2014 &nbsp;&nbsp;Tidy Harbor. &nbsp;All rights reserved &nbsp;&nbsp;/ &nbsp;&nbsp;Terms and Conditions</div>

</body>
</html>
```